Interior design service, along with home organization, packing, and staging, home and business. As well as staging in conjunction with real estate sales.
Updates

Love many of your designs and will be choosing today. To inform you of the exact details needed, the name of the company is "Touches by Marla T" , my phone number and e-,ail need to be included. i also need either description or some sort of bullet points that give an idea of the following:

- Interior design for home and business
- Home organization and packing
- Staging for personal and professional space
- Real estate stagingĀ 

Thank you

Target Market(s)

wide audience, but most importantly people looking for a quality service

Industry/Entity Type

Real Estate

Contact Information for Business Card

Touches By Marla T
Marla Tovendi
(555)614-2937
mtbrook@mailnest.example

Requirements
Must have
• I'm 29 so i want my card to reflect something professional but still fresh. I don't have any specific photos or quotes that Ive included, however I like the card to reflect a personal touch, which is what I'm seeking from this service in the design of my card. Thanks!

```html
<!DOCTYPE html>
<html lang="en">
<head>
<meta charset="utf-8">
<title>Touches by Marla T – Business Card</title>
<link rel="stylesheet" href="https://fonts.googleapis.com/css2?family=Dancing+Script:wght@600&family=Questrial&display=swap">
<style>
  :root {
    --backdrop: #eeeeee;
    --card-centre: #987799;
    --card-edge: #7f5f86;
    --ink-light: #dccfd9;
    --rule: #cdbfcb;
    --card-shadow: rgba(40, 20, 45, 0.22);
  }
  * { margin: 0; padding: 0; box-sizing: border-box; }
  html, body {
    width: 1200px;
    height: 702px;
    overflow: hidden;
    background: var(--backdrop);
  }
  .canvas {
    width: 1200px;
    height: 702px;
    display: flex;
    align-items: center;
    justify-content: center;
    gap: 60px;
  }
  .card {
    position: relative;
    width: 500px;
    height: 286px;
    background: radial-gradient(ellipse at 50% 35%, var(--card-centre) 0%, var(--card-edge) 85%);
    box-shadow: 0 14px 30px var(--card-shadow);
    color: var(--ink-light);
    overflow: hidden;
  }
  .card-front {
    display: flex;
    flex-direction: column;
    align-items: center;
    justify-content: center;
    gap: 10px;
  }
  .owner-name {
    font-family: "Dancing Script", cursive;
    font-weight: 600;
    font-size: 62px;
    line-height: 1.1;
    letter-spacing: 1px;
    color: var(--ink-light);
  }
  .company-name {
    font-family: "Questrial", sans-serif;
    font-weight: 400;
    font-size: 15px;
    letter-spacing: 2px;
    color: var(--ink-light);
  }
  .card-back {
    font-family: "Questrial", sans-serif;
    font-size: 14px;
    line-height: 1.55;
  }
  .contact {
    position: absolute;
    left: 28px;
    top: 112px;
    list-style: none;
    white-space: nowrap;
  }
  .contact li { margin-bottom: 6px; }
  .divider {
    position: absolute;
    left: 282px;
    top: 36px;
    width: 1.5px;
    height: 218px;
    background: var(--rule);
  }
  .services {
    position: absolute;
    left: 298px;
    top: 44px;
    list-style: none;
    white-space: nowrap;
  }
  .services li { line-height: 1.55; }
</style>
</head>
<body>
  <main class="canvas">
    <section class="card card-front" aria-label="Card front">
      <h1 class="owner-name">Marla Tovendi</h1>
      <p class="company-name">Touches by Marla T</p>
    </section>
    <section class="card card-back" aria-label="Card back">
      <ul class="contact">
        <li>Phone: (555)614-2937</li>
        <li>Email: mtbrook@mailnest.example</li>
      </ul>
      <div class="divider"></div>
      <ul class="services">
        <li>Interior Design Service</li>
        <li>Home Organization</li>
        <li>Packing</li>
        <li>Staging</li>
        <li>Home and Business</li>
        <li>Real Estate Sales</li>
      </ul>
    </section>
  </main>
</body>
</html>
```